Need a business card for our overland brand!

We had the logo made and we need a great design for our business card. Use the logo provide or tweak it however you see fit.

Contact Information for Business Card

Name, Title, Telephone, email, website

```html
<!DOCTYPE html>
<html lang="en">
<head>
<meta charset="utf-8">
<title>Ridgeline Expeditions – Business Card</title>
<link rel="stylesheet" href="https://fonts.googleapis.com/css2?family=Montserrat:wght@400;700&display=swap">
<style>
  :root {
    --canvas: #ababab;
    --navy: #243750;
    --teal: #1fa3c4;
    --white: #ffffff;
    --ink: #243750;
  }
  * { box-sizing: border-box; margin: 0; padding: 0; }
  html, body { width: 1200px; height: 1000px; overflow: hidden; }
  body {
    background: var(--canvas);
    font-family: "Montserrat", Arial, sans-serif;
    position: relative;
  }
  .card {
    position: absolute;
    top: 194px;
    width: 352px;
    height: 612px;
    border-radius: 24px;
    overflow: hidden;
  }
  .card--back { left: 266px; background: var(--navy); }
  .card--front { left: 645px; background: var(--white); }

  .brand-name {
    position: absolute;
    left: 0; right: 0;
    text-align: center;
    font-weight: 700;
    text-transform: uppercase;
    line-height: 1.05;
    letter-spacing: 0.5px;
  }
  .card--back .brand-name { top: 282px; color: var(--white); font-size: 22px; }
  .card--front .brand-name { top: 500px; color: var(--navy); font-size: 24px; }

  .peak-art {
    position: absolute;
    left: 0; top: 0;
    width: 100%; height: 232px;
    background: linear-gradient(170deg, var(--navy) 55%, var(--teal) 100%);
  }

  .contact {
    position: absolute;
    top: 272px;
    left: 0; right: 0;
    text-align: center;
    color: var(--ink);
  }
  .contact__name { font-weight: 700; font-size: 16px; line-height: 24px; }
  .contact__title { font-size: 16px; line-height: 22px; }
  .contact__icons {
    display: flex;
    justify-content: center;
    gap: 4px;
    margin: 6px 0 6px;
  }
  .contact__icons svg { width: 24px; height: 24px; display: block; }
  .contact__line { font-size: 14px; line-height: 18px; letter-spacing: 0.3px; }
</style>
</head>
<body>

  <section class="card card--back">
    <div class="brand-name">Ridgeline<br>Expeditions</div>
  </section>

  <section class="card card--front">
    <div class="peak-art" role="img" aria-label="Snow-capped mountain peak illustration against a dark navy sky"></div>

    <div class="contact">
      <p class="contact__name">Name Surname</p>
      <p class="contact__title">Title</p>
      <div class="contact__icons">
        <svg viewBox="0 0 24 24" aria-label="Phone">
          <circle cx="12" cy="12" r="12" fill="var(--teal)"/>
          <path d="M8.6 6.8l1.6-.3 1 2.4-1.1.9a6.5 6.5 0 0 0 3.1 3.1l.9-1.1 2.4 1-.3 1.6c-.1.5-.6.8-1.1.8A8.3 8.3 0 0 1 7.8 7.9c0-.5.3-1 .8-1.1z" fill="var(--white)"/>
        </svg>
        <svg viewBox="0 0 24 24" aria-label="Email">
          <circle cx="12" cy="12" r="12" fill="var(--teal)"/>
          <rect x="7" y="8.5" width="10" height="7" rx="1" fill="var(--white)"/>
          <path d="M7.3 9l4.7 3.5L16.7 9" fill="none" stroke="var(--teal)" stroke-width="1"/>
        </svg>
        <svg viewBox="0 0 24 24" aria-label="Website">
          <circle cx="12" cy="12" r="12" fill="var(--teal)"/>
          <g fill="none" stroke="var(--white)" stroke-width="1.1">
            <circle cx="12" cy="12" r="5.5"/>
            <ellipse cx="12" cy="12" rx="2.4" ry="5.5"/>
            <path d="M6.5 12h11M7.3 9.2h9.4M7.3 14.8h9.4"/>
          </g>
        </svg>
      </div>
      <p class="contact__line">1234-567-890</p>
      <p class="contact__line">email@website.com</p>
      <p class="contact__line">website.com</p>
    </div>

    <div class="brand-name">Ridgeline<br>Expeditions</div>
  </section>

</body>
</html>
```